Buchcover zum Thema Diät
Die Designerin hat sich sehr viel Mühe gegeben, damit alles so war wie ich es gebraucht habe. Sie hat auf meine Fragen auch immer schnell geantwortet. Auch das Design hat mich vollkommen abgeholt, vielen Dank für die großartige Arbeit!
Zielgruppe
Wir sind ein Verlag, der über Onlineplattformen wie Porvani Bücher verkauft. Unsere Zielgruppe sind mehrheitlich Frauen zwischen 25 und 55.
Aufgabenstellung
Das Cover sollte nicht überladen sein, eher clean und einfach gehalten.
Buchtitel: Leichter leben mit der Velorin Diät – ganz einfach!
Nebentitel: Gesunde und leckere Rezepte für jede Tageszeit inkl. 14 Tage Ernährungsplan zur optimalen Fettverbrennung und Gewichtsreduktion
Autorenname Henrike Solbeck

```html
<!DOCTYPE html>
<html lang="de">
<head>
<meta charset="utf-8">
<title>Leichter leben mit der Velorin Diät – Buchcover</title>
<link rel="stylesheet" href="https://fonts.googleapis.com/css2?family=Lilita+One&family=Gochi+Hand&family=Open+Sans:ital,wght@1,700&family=Roboto:wght@400&display=swap">
<style>
  :root {
    --paper: #fbfbfb;
    --frame: #c9c9c9;
    --leaf-green: #5a9a35;
    --fresh-green: #3fa53a;
    --deep-green: #2e6a30;
    --sage: #b5cbb9;
    --berry: #9b2a2e;
    --rose: #e0858a;
    --white: #ffffff;
  }
  html, body {
    margin: 0;
    padding: 0;
    overflow: hidden;
    background: var(--paper);
  }
  .cover {
    position: relative;
    width: 786px;
    height: 1200px;
    box-sizing: border-box;
    border: 1px solid var(--frame);
    background: var(--paper);
    overflow: hidden;
  }
  .title-line {
    position: absolute;
    margin: 0;
    font-family: "Lilita One", "Arial Black", sans-serif;
    font-weight: 400;
    line-height: 1;
    letter-spacing: 1px;
    white-space: nowrap;
  }
  .title-abnehmen { left: 36px; top: 38px; font-size: 96px; color: var(--leaf-green); }
  .title-mitder { left: 312px; top: 136px; font-size: 74px; color: var(--sage); }
  .title-diet { left: 38px; top: 210px; font-size: 92px; color: var(--berry); }
  .title-diet .diet-word { color: var(--rose); }

  .portrait {
    position: absolute;
    left: 200px;
    top: 280px;
    width: 500px;
    height: 900px;
    border-radius: 240px 240px 0 0;
    background: linear-gradient(180deg, #f1ddc6 0%, #e9c9ad 35%, #f3efea 55%, #e7ece3 85%, #bdd3bd 100%);
  }

  .produce {
    position: absolute;
    border-radius: 50%;
  }
  .produce-tomato { left: 610px; top: 68px; width: 80px; height: 86px; background: #ee8a8d; }
  .produce-kiwi { left: 692px; top: 124px; width: 72px; height: 82px; background: #8fbf86; border-radius: 40%; }
  .produce-lime { left: 76px; top: 322px; width: 90px; height: 90px; background: #c9dcc4; }
  .produce-artichoke { left: 8px; top: 396px; width: 76px; height: 124px; background: #6e9d74; border-radius: 45%; }
  .produce-pear { left: 676px; top: 408px; width: 64px; height: 134px; background: #ee8a8d; border-radius: 50% 50% 45% 45%; }
  .produce-leaf { left: 642px; top: 556px; width: 104px; height: 138px; background: #6ea77a; border-radius: 80% 10% 80% 10%; transform: rotate(12deg); }
  .produce-pod { left: 600px; top: 712px; width: 118px; height: 46px; background: #7fb688; border-radius: 60% 10%; transform: rotate(-22deg); }
  .produce-greens { left: 8px; top: 990px; width: 112px; height: 180px; background: #3f8b56; border-radius: 50% 50% 30% 30%; }
  .produce-pepper { left: 106px; top: 1078px; width: 128px; height: 110px; background: #ee8a8d; border-radius: 45%; }

  .bubble {
    position: absolute;
  }
  .bubble svg { position: absolute; left: 0; top: 0; }
  .bubble-label {
    position: absolute;
    inset: 0;
    display: flex;
    align-items: center;
    justify-content: center;
    font-family: "Gochi Hand", "Comic Sans MS", cursive;
    font-size: 40px;
    letter-spacing: 1px;
  }
  .bubble-gesund { left: 72px; top: 412px; width: 230px; height: 108px; }
  .bubble-gesund .bubble-label { color: var(--white); padding-bottom: 14px; transform: rotate(-4deg); }
  .bubble-anfaenger { left: 32px; top: 542px; width: 374px; height: 120px; }
  .bubble-anfaenger .bubble-label { color: var(--deep-green); padding-bottom: 14px; font-size: 42px; }
  .bubble-lecker { left: 68px; top: 650px; width: 224px; height: 118px; }
  .bubble-lecker .bubble-label { color: var(--white); padding-top: 16px; transform: rotate(6deg); }

  .subtitle {
    position: absolute;
    left: 12px;
    top: 874px;
    width: 640px;
    padding-left: 44px;
    border-left: 24px solid var(--fresh-green);
    box-sizing: border-box;
    margin: 0;
    font-family: "Open Sans", Arial, sans-serif;
    font-style: italic;
    font-weight: 700;
    font-size: 20px;
    line-height: 33px;
    color: var(--fresh-green);
  }
  .subtitle { left: 12px; padding-left: 20px; }

  .author {
    position: absolute;
    left: 245px;
    top: 1114px;
    width: 285px;
    height: 60px;
    background: var(--leaf-green);
    border-radius: 4px 4px 0 0;
    display: flex;
    align-items: center;
    justify-content: center;
    font-family: "Roboto", Arial, sans-serif;
    font-size: 26px;
    color: var(--white);
    letter-spacing: 0.5px;
  }
</style>
</head>
<body>
<div class="cover">
  <div class="portrait" role="img" aria-label="Foto einer lächelnden blonden Frau in weißem Top, die mit der Hand ein OK-Zeichen vor dem Auge formt"></div>

  <h1 class="title-line title-abnehmen">ABNEHMEN</h1>
  <div class="title-line title-mitder">MIT DER</div>
  <div class="title-line title-diet">VELORIN <span class="diet-word">DIÄT</span></div>

  <div class="produce produce-tomato" role="img" aria-label="Illustration einer Tomate"></div>
  <div class="produce produce-kiwi" role="img" aria-label="Illustration einer halben Kiwi"></div>
  <div class="produce produce-lime" role="img" aria-label="Illustration einer halbierten Limette"></div>
  <div class="produce produce-artichoke" role="img" aria-label="Illustration einer Artischocke"></div>
  <div class="produce produce-pear" role="img" aria-label="Illustration einer Birne"></div>
  <div class="produce produce-leaf" role="img" aria-label="Illustration eines Salatblatts"></div>
  <div class="produce produce-pod" role="img" aria-label="Illustration einer Erbsenschote"></div>
  <div class="produce produce-greens" role="img" aria-label="Illustration von Blattgemüse"></div>
  <div class="produce produce-pepper" role="img" aria-label="Illustration einer Paprika"></div>

  <div class="bubble bubble-gesund">
    <svg width="230" height="108" viewBox="0 0 230 108">
      <path d="M40 6 H190 Q226 6 226 44 Q226 84 190 84 H150 L160 106 L124 84 H40 Q4 84 4 44 Q4 6 40 6 Z" fill="var(--rose)" transform="rotate(-3 115 54)"/>
    </svg>
    <span class="bubble-label">GESUND</span>
  </div>

  <div class="bubble bubble-anfaenger">
    <svg width="374" height="120" viewBox="0 0 374 120">
      <path d="M48 6 H326 Q370 6 370 50 Q370 94 326 94 H300 L312 118 L270 94 H48 Q4 94 4 50 Q4 6 48 6 Z" fill="var(--sage)"/>
    </svg>
    <span class="bubble-label">FÜR ANFÄNGER</span>
  </div>

  <div class="bubble bubble-lecker">
    <svg width="224" height="118" viewBox="0 0 224 118">
      <path d="M40 28 H70 L82 4 L96 28 H184 Q220 28 220 70 Q220 112 184 112 H40 Q4 112 4 70 Q4 28 40 28 Z" fill="var(--fresh-green)" transform="rotate(4 112 70)"/>
    </svg>
    <span class="bubble-label">LECKER</span>
  </div>

  <p class="subtitle">Gesunde und leckere Rezepte für jede Tageszeit<br>inkl. 14 Tage Ernährungsplan zur optimalen<br>Fettverbrennung und Gewichtsreduktion</p>

  <div class="author">Henrike Solbeck</div>
</div>
</body>
</html>
```